メインデザインを依頼させていただきます。

容器はいろいろありますが、中の一種類だけの寸法を提供します。これをベースにデザインの設計をお願いいたします。

中国や他東南アジアにも販売予定ですので、デザイン中の文字であれば、基本的に英語にお願いします。

ナチュラル、オリーブ、明快、おしゃれ、などイメージがほしいです。
部屋いおいても気分転換、おしゃれと感じるデザインがいいです。

記載項目
紙箱
サイズ:W47mm×D47mm×H190mm

容器寸法は

```html
<!DOCTYPE html>
<html lang="en">
<head>
<meta charset="UTF-8">
<title>Verdia — Package Front</title>
<link rel="stylesheet" href="https://fonts.googleapis.com/css2?family=Cormorant+Garamond:wght@500&display=swap">
<style>
  :root {
    --frame-pink: #f7d4f3;
    --frame-white: #ffffff;
    --lavender: #d8b4f3;
    --ring-light: #fde9fb;
    --ring-mid: #f6cdef;
    --ring-deep: #eebce6;
    --name-teal: #5cc9d0;
    --leaf-white: rgba(255, 255, 255, 0.92);
  }
  html, body {
    margin: 0;
    padding: 0;
    width: 1200px;
    height: 2208px;
    overflow: hidden;
    background: var(--frame-pink);
  }
  .package-front {
    position: relative;
    width: 1200px;
    height: 2208px;
    background: var(--frame-pink);
  }
  .panel {
    position: absolute;
    left: 84px;
    top: 76px;
    width: 1008px;
    height: 2032px;
    background: var(--lavender);
    border: 12px solid var(--frame-white);
    overflow: hidden;
  }
  .corner-rings {
    position: absolute;
  }
  .corner-rings.top-left {
    left: 0;
    top: 0;
  }
  .corner-rings.bottom-right {
    right: 0;
    bottom: 0;
  }
  .olive-branch {
    position: absolute;
    background: radial-gradient(ellipse at 55% 45%, var(--leaf-white) 0%, rgba(255,255,255,0.75) 45%, rgba(255,255,255,0) 72%);
    border-radius: 50%;
  }
  .olive-branch.upper {
    left: 500px;
    top: 140px;
    width: 400px;
    height: 470px;
  }
  .olive-branch.lower {
    left: 150px;
    top: 1600px;
    width: 220px;
    height: 240px;
  }
  .name-block {
    position: absolute;
    left: 0;
    width: 100%;
    margin: 0;
    text-align: center;
    font-family: "Cormorant Garamond", serif;
    font-weight: 500;
    font-style: normal;
    color: var(--name-teal);
    line-height: 1;
  }
  .product-name {
    top: 900px;
    font-size: 200px;
    letter-spacing: 12px;
  }
  .brand-line {
    top: 1150px;
    font-size: 76px;
    letter-spacing: 4px;
  }
</style>
</head>
<body>
  <main class="package-front">
    <section class="panel">
      <svg class="corner-rings top-left" width="360" height="360" viewBox="0 0 360 360" aria-hidden="true">
        <circle cx="0" cy="0" r="340" fill="var(--ring-deep)"/>
        <circle cx="0" cy="0" r="320" fill="var(--ring-mid)"/>
        <circle cx="0" cy="0" r="295" fill="var(--ring-light)"/>
        <circle cx="0" cy="0" r="265" fill="#ffffff"/>
      </svg>

      <div class="olive-branch upper" role="img" aria-label="White olive branch with leaves and fruit"></div>

      <h1 class="name-block product-name">Verdia</h1>
      <p class="name-block brand-line">by lumera</p>

      <div class="olive-branch lower" role="img" aria-label="Small white olive sprig"></div>

      <svg class="corner-rings bottom-right" width="520" height="520" viewBox="0 0 520 520" aria-hidden="true">
        <circle cx="520" cy="520" r="500" fill="var(--ring-deep)"/>
        <circle cx="520" cy="520" r="470" fill="var(--ring-mid)"/>
        <circle cx="520" cy="520" r="440" fill="var(--ring-light)"/>
        <circle cx="520" cy="520" r="405" fill="#ffffff"/>
      </svg>
    </section>
  </main>
</body>
</html>
```